Business Card Design

I need a new business card design for myself. I am a life coach and therapist with both a private practice and now a newly formed business see both my websites: I am looking for a business card to support this and be close to the colours and design of my private practice website and my business website. I am looking for strong bright nature based colours. Sun, Sea and Greenery. The card should reflect inspiration, enlightenment, empowerment and strength!!!
www.helenagracewarrick.com and
www.calmer-paths-mentoring.co.uk
Updates
Thank you everyone for your designs. I will be making a final decision by the end of this week and will notify you as soon as possible after this.
Industry/Entity Type
Business
Contact Information for Business Card
Helena Grace Warrick, BSc, PGDip & MRes
Therapist and Life Coach
Calmer Paths Mentoring
17 Larkspur Road
Manchester
M4 7QT
0800 0619483 Mobile: 07700948216
email: hgwarrick@helenagracewarrick.com
Requirements
Must have
- not too busy. To be clear and easy to read information..
and to include this tag line:
"helping you live your life with passion and confidence"

```html
<!DOCTYPE html>
<html lang="en">
<head>
<meta charset="utf-8">
<title>Helena Grace Warrick – Business Card</title>
<link href="https://fonts.googleapis.com/css2?family=Questrial&display=swap" rel="stylesheet">
<style>
  :root {
    --page-bg: #ffffff;
    --card-white: #ffffff;
    --card-grey: #e9e9e9;
    --brand-green: #2f8f3c;
    --deep-green: #13813a;
    --light-green: #44a04e;
    --sky-blue: #1a8fd6;
    --faint-green: #5cb85f;
    --tagline: #ffffff;
  }
  * { box-sizing: border-box; margin: 0; padding: 0; }
  html, body {
    width: 1200px;
    height: 900px;
    overflow: hidden;
    background: var(--page-bg);
    font-family: "Questrial", "Century Gothic", sans-serif;
  }
  .stage {
    position: relative;
    width: 1200px;
    height: 900px;
  }
  .card {
    position: absolute;
    top: 296px;
    width: 540px;
    height: 308px;
    border-radius: 24px;
    overflow: hidden;
    box-shadow: 0 6px 18px rgba(0, 0, 0, 0.12);
  }
  /* Front */
  .card-front {
    left: 42px;
    background: linear-gradient(to bottom, var(--card-grey) 0%, var(--card-white) 45%, var(--card-white) 100%);
  }
  .front-name {
    position: absolute;
    left: 28px;
    top: 26px;
    font-size: 33px;
    color: var(--brand-green);
    letter-spacing: 0.2px;
  }
  .front-credentials {
    position: absolute;
    left: 46px;
    top: 92px;
    font-size: 14.5px;
    line-height: 19px;
    color: var(--sky-blue);
  }
  .contact-list {
    position: absolute;
    left: 18px;
    top: 186px;
    list-style: none;
    font-size: 15.5px;
    line-height: 19px;
    color: var(--deep-green);
  }
  .contact-list li {
    display: flex;
    align-items: center;
    gap: 4px;
  }
  .contact-icon {
    width: 14px;
    height: 14px;
    flex: none;
  }
  .front-band-blue {
    position: absolute;
    left: 0;
    right: 0;
    bottom: 22px;
    height: 5px;
    background: var(--sky-blue);
  }
  .front-band-green {
    position: absolute;
    left: 0;
    right: 0;
    bottom: 0;
    height: 22px;
    background: var(--deep-green);
  }
  /* Back */
  .card-back {
    left: 618px;
    background: linear-gradient(to bottom, var(--light-green) 0%, #2c9243 50%, var(--deep-green) 100%);
  }
  .back-tagline {
    position: absolute;
    left: 0;
    right: 0;
    top: 130px;
    text-align: center;
    font-size: 17.5px;
    color: var(--tagline);
  }
  .back-name {
    position: absolute;
    right: 24px;
    bottom: 56px;
    font-size: 22px;
    color: var(--faint-green);
  }
</style>
</head>
<body>
<main class="stage">

  <section class="card card-front" aria-label="Business card front">
    <h1 class="front-name">Helena Grace Warrick</h1>
    <p class="front-credentials">BSc, PGDip &amp; MRes Therapist and<br>Life Coach Calmer Paths Mentoring</p>

    <ul class="contact-list">
      <li>
        <svg class="contact-icon" viewBox="0 0 16 16" aria-hidden="true">
          <path d="M3 1.5l3 .5 1 3.5-2 1.2a9 9 0 0 0 4.3 4.3l1.2-2 3.5 1 .5 3-2 1.5C7.5 14 2 8.5 1.5 3.5z" fill="var(--sky-blue)"/>
        </svg>
        07700948216
      </li>
      <li>
        <svg class="contact-icon" viewBox="0 0 16 16" aria-hidden="true">
          <rect x="1" y="3.5" width="14" height="9.5" rx="1" fill="var(--sky-blue)"/>
          <path d="M1.5 4.2 8 9l6.5-4.8" stroke="#fff" stroke-width="1.3" fill="none"/>
        </svg>
        hgwarrick@helenagracewarrick.com
      </li>
      <li>
        <svg class="contact-icon" viewBox="0 0 16 16" aria-hidden="true">
          <circle cx="8" cy="8" r="6.5" fill="none" stroke="var(--sky-blue)" stroke-width="1.4"/>
          <ellipse cx="8" cy="8" rx="2.8" ry="6.5" fill="none" stroke="var(--sky-blue)" stroke-width="1.2"/>
          <path d="M1.5 8h13M2.6 4.8h10.8M2.6 11.2h10.8" stroke="var(--sky-blue)" stroke-width="1.1"/>
        </svg>
        www.helenagracewarrick.com
      </li>
      <li>
        <svg class="contact-icon" viewBox="0 0 16 16" aria-hidden="true">
          <circle cx="8" cy="8" r="6.5" fill="none" stroke="var(--sky-blue)" stroke-width="1.4"/>
          <ellipse cx="8" cy="8" rx="2.8" ry="6.5" fill="none" stroke="var(--sky-blue)" stroke-width="1.2"/>
          <path d="M1.5 8h13M2.6 4.8h10.8M2.6 11.2h10.8" stroke="var(--sky-blue)" stroke-width="1.1"/>
        </svg>
        www.calmer-paths-mentoring.co.uk
      </li>
      <li>
        <svg class="contact-icon" viewBox="0 0 16 16" aria-hidden="true">
          <path d="M8 1.5 1 8h2v6.5h4v-4h2v4h4V8h2z" fill="var(--sky-blue)"/>
        </svg>
        17 Larkspur Road Manchester M4 7QT 0800 0619483
      </li>
    </ul>

    <div class="front-band-blue"></div>
    <div class="front-band-green"></div>
  </section>

  <section class="card card-back" aria-label="Business card back">
    <p class="back-tagline">"helping you live your life with passion and confidence"</p>
    <p class="back-name">Helena Grace Warrick</p>
  </section>

</main>
</body>
</html>
```